KTB - Redesign (PSD Files Only)

Requirements for the site:

1. We need our logo recreated, please use the same design and change colors to work on a white background

2. The site is a "Wizard" based site, that takes the customer through the process of creating a unique web presence that suits there needs

3.Colors Needed - Main "Dark Blue" Secondary = "Dark Grey" -Other = "Light Grey and White"

4.We need a CRISP CLEAN DESIGN, simple design

5.Wireframes are a general layout and may be modified by you to enhance the design

6. We want a complete web 5.0 look with big buttons and text boxes

7.The more personality the better

8. Current Site brightlarkworks.example

9.See attachments for wireframes

10. Designer should deliver PSD files, no coding is required

11. The portfolio wireframe, should look like the design of the pixelharbor portfolio template
Updates

KEEP IT SIMPLE.,.....

We like the moonquill scaffold style of designs

```html
<!DOCTYPE html>
<html lang="en">
<head>
<meta charset="utf-8">
<title>KTB – Custom Website Design</title>
<link href="https://fonts.googleapis.com/css2?family=Open+Sans:wght@400;600;700&display=swap" rel="stylesheet">
<style>
:root{
  --blue:#0f4f9c;
  --blue-light:#a9c4e4;
  --grey-dark:#3a3a3a;
  --grey-card:#404040;
  --grey-text:#666;
  --grey-hero:#ececec;
  --grey-input:#efefef;
  --white:#fff;
  --bullet:#a8a8a8;
}
*{margin:0;padding:0;box-sizing:border-box}
html,body{width:1200px;height:1111px;overflow:hidden;background:var(--white);font-family:"Open Sans",sans-serif;color:var(--grey-text)}
.page{position:relative;width:1200px;height:1111px}
.abs{position:absolute}

.topbar{left:0;top:0;width:1200px;height:35px;background:var(--grey-dark)}
.nav{left:200px;top:0;height:35px;display:flex;gap:23px;align-items:center;font-size:13.5px;color:#c8c8c8}
.social{left:563px;top:8px;display:flex;gap:6px}
.social span{width:19px;height:19px;border-radius:50%;background:#8a8a8a;display:block}
.phone{right:198px;top:0;height:35px;display:flex;align-items:center;gap:4px;font-size:13.5px;color:#c8c8c8}

.hero{left:0;top:35px;width:1200px;height:149px;background:var(--grey-hero);text-align:center}
.hero h1{margin-top:17px;font-size:29px;font-weight:600;letter-spacing:-1.2px;color:var(--blue)}
.hero h2{margin-top:16px;font-size:19.5px;font-weight:600;letter-spacing:-.8px;color:#333}
.hero p{width:520px;margin:2px auto 0;font-size:12.3px;line-height:14.5px;color:#777}

.feature{text-align:center;font-size:14px;line-height:17.5px;letter-spacing:-.6px;color:#666;width:160px}
.feature svg{display:block;margin:0 auto 6px}

.logo{left:555px;top:208px;width:90px;text-align:center;color:var(--blue)}
.logo .mark{font-size:34px;font-weight:700;letter-spacing:-1px;line-height:36px}
.logo .sub{font-size:8px;color:var(--blue);line-height:10px}

.step{left:520px;top:411px;width:160px;text-align:center;font-size:11px;color:#777}
.progress{left:520px;top:430px;width:160px;height:14px;background:var(--blue-light)}
.progress i{display:block;width:37px;height:14px;background:var(--blue)}
.project-input{left:370px;top:465px;width:292px;height:36px;background:var(--grey-input);border:1px solid #ddd;border-top:2px solid #ccc;font-size:11.5px;color:#999;padding:9px 8px}
.start-btn{left:671px;top:465px;width:159px;height:36px;background:var(--blue);color:var(--white);font-size:19px;font-weight:600;letter-spacing:-1px;text-align:center;line-height:35px}

.rule{left:0;width:1200px;border-top:1px dashed #d6d6d6}

.card{top:562px;width:187px;height:215px;background:var(--grey-card);color:#e8e8e8;font-size:11.2px;line-height:13.6px}
.card .tab{position:absolute;left:-8px;top:8px;width:185px;height:30px;background:var(--white);color:var(--blue);font-size:17.5px;font-weight:600;letter-spacing:-.9px;line-height:30px;padding-left:17px;clip-path:polygon(0 0,176px 0,185px 15px,176px 30px,0 30px)}
.card .fold{position:absolute;left:-8px;top:38px;width:8px;height:6px;background:#9a9a9a;clip-path:polygon(0 0,100% 0,100% 100%)}
.card .intro{position:absolute;left:9px;top:49px;width:172px}
.card ul{position:absolute;left:9px;top:99px;width:172px;list-style:none;color:var(--bullet);font-size:10.3px;line-height:15.2px}
.card li{padding-left:10px;position:relative;line-height:11px;margin-bottom:4.2px}
.card li::before{content:"•";position:absolute;left:0}

.thumb{top:835px;width:193px;height:193px;border:4px solid #dcdcdc}
.thumb div{width:100%;height:100%}
.arrow{top:902px}

.footer{left:0;top:1060px;width:1200px;height:51px;background:var(--blue);color:#c9d8ee;font-size:11.3px}
.footer .copy{position:absolute;left:199px;top:18px}
.footer .copy b{font-weight:400;color:var(--white)}
.badge{position:absolute;left:912px;top:10px;width:89px;height:32px;background:var(--white)}
.badge i{display:block;width:30px;height:32px;background:#3a6fc0}
</style>
</head>
<body>
<div class="page">

  <div class="abs topbar"></div>
  <nav class="abs nav"><span>Home</span><span>About Us</span><span>Portfolio</span><span>Contact Us</span></nav>
  <div class="abs social" aria-hidden="true"><span></span><span></span><span></span></div>
  <div class="abs phone">
    <svg width="11" height="11" viewBox="0 0 24 24"><path fill="#c8c8c8" d="M6.6 10.8a15 15 0 0 0 6.6 6.6l2.2-2.2c.3-.3.7-.4 1-.2 1.1.4 2.3.6 3.6.6.6 0 1 .4 1 1V20c0 .6-.4 1-1 1A17 17 0 0 1 3 4c0-.6.4-1 1-1h3.5c.6 0 1 .4 1 1 0 1.3.2 2.5.6 3.6.1.3 0 .7-.2 1z"/></svg>
    1-800-555-0142
  </div>

  <header class="abs hero">
    <h1>Get A Custom Website Design In 21 Days Or LESS!</h1>
    <h2>Find out why we’re the #1 custom website design marketplace.</h2>
    <p>Our network of designers will create 50+ web design samples for you to choose and our marketing experts will pave the way for your success.</p>
  </header>

  <div class="abs feature" style="left:243px;top:232px">
    <svg width="34" height="36" viewBox="0 0 34 36"><path d="M5 18a12 12 0 0 1 24 0" fill="none" stroke="var(--blue)" stroke-width="4"/><rect x="2" y="16" width="7" height="11" rx="2" fill="var(--blue)"/><rect x="25" y="16" width="7" height="11" rx="2" fill="var(--blue)"/><path d="M28 27q0 6-8 6" fill="none" stroke="var(--blue)" stroke-width="2.5"/><circle cx="19" cy="33" r="2.5" fill="var(--blue)"/></svg>
    24/7 Customer<br>Support
  </div>

  <div class="abs logo">
    <div class="mark">KTB</div>
    <div class="sub">Kestrel Tide Bureau</div>
  </div>

  <div class="abs feature" style="left:790px;top:232px">
    <svg width="34" height="36" viewBox="0 0 34 36"><rect x="2" y="16" width="7" height="16" rx="1" fill="var(--blue)"/><path d="M11 16l6-10c2-3 5-2 5 1l-1 7h8c2 0 4 2 3 4l-3 11c-1 2-2 3-4 3H11z" fill="var(--blue)"/></svg>
    100% Moneyback<br>Gaurantee
  </div>

  <div class="abs feature" style="left:423px;top:314px">
    <svg width="42" height="34" viewBox="0 0 42 34"><path d="M16 4h18a6 6 0 0 1 6 6v8a6 6 0 0 1-6 6h-2l1 6-7-6H16a6 6 0 0 1-6-6v-8a6 6 0 0 1 6-6z" fill="#5a8fd0"/><path d="M8 2h18a6 6 0 0 1 6 6v8a6 6 0 0 1-6 6H14l-7 6 1-6a6 6 0 0 1-6-6V8a6 6 0 0 1 6-6z" fill="var(--blue)"/><text x="11" y="18" font-size="14" font-weight="700" fill="#fff" font-family="Open Sans,sans-serif">”</text></svg>
    100% No Obligation<br>Free Web Quote
  </div>

  <div class="abs feature" style="left:617px;top:314px">
    <svg width="34" height="34" viewBox="0 0 34 34"><path d="M12 6H4v25h26V6h-8" fill="none" stroke="var(--blue)" stroke-width="3.5"/><path d="M17 2v18M11 14l6 7 6-7" fill="none" stroke="var(--blue)" stroke-width="4"/></svg>
    Save 1000’s On<br>Web Design
  </div>

  <svg class="abs" style="left:300px;top:360px" width="160" height="130" viewBox="0 0 160 130" aria-hidden="true">
    <path d="M152 8C90-8 30 10 12 40s10 70 45 80" fill="none" stroke="#999" stroke-width="1" stroke-dasharray="4 3"/>
    <path d="M50 112l8 8-10 4" fill="none" stroke="#999" stroke-width="1"/>
  </svg>

  <div class="abs step">Step 1</div>
  <div class="abs progress"><i></i></div>
  <div class="abs project-input">Name Your Project...</div>
  <div class="abs start-btn">Start Your Project</div>

  <div class="abs rule" style="top:530px"></div>

  <section class="abs card" style="left:207px">
    <div class="tab">Why Choose KTB?</div><div class="fold"></div>
    <p class="intro">We are a full service design &amp; marketingcompany tha will handle everything.</p>
    <ul style="top:99px"><li>Dedicated Project</li><li>Manager</li><li>Single Point Contact</li><li>Low Cost</li><li>50+ Design Samples for you to choose.</li></ul>
  </section>
  <section class="abs card" style="left:410px">
    <div class="tab">Web Services</div><div class="fold"></div>
    <p class="intro">We specialize in the following design services:</p>
    <ul><li>Web Design</li><li>Ecommerce Design</li><li>Web Programming</li><li>Logo Design</li><li>Stationary/Print Design</li><li>Ad Design</li><li>Email Template Design.</li></ul>
  </section>
  <section class="abs card" style="left:612px">
    <div class="tab">Marketing Services</div><div class="fold"></div>
    <p class="intro">We handle all online marketing including the following:</p>
    <ul><li>Search Ad Campaigns</li><li>Local Map Marketing</li><li>Search Engine Optimization</li><li>Email Marketing</li><li>Social Media Marketing.</li></ul>
  </section>
  <section class="abs card" style="left:814px">
    <div class="tab">Maintainence Services</div><div class="fold"></div>
    <p class="intro">Let us maintain your site and save up to 50% on the following:</p>
    <ul><li>Website Hosting</li><li>Software Upgrades</li><li>Custom Web Programming</li><li>Website Marketing</li></ul>
  </section>

  <div class="abs rule" style="top:806px"></div>

  <svg class="abs arrow" style="left:177px" width="14" height="56" viewBox="0 0 14 56" aria-hidden="true"><path d="M13 1L1 28l12 27" fill="none" stroke="#aaa" stroke-width="1.2"/></svg>
  <div class="abs thumb" style="left:200px"><div role="img" aria-label="Portfolio sample: restaurant website with warm food photography" style="background:linear-gradient(160deg,#c89a4a,#b5452a 60%,#d6a64b)"></div></div>
  <div class="abs thumb" style="left:403px"><div role="img" aria-label="Portfolio sample: cafe website with light layout and food photo" style="background:linear-gradient(180deg,#fafafa 0%,#f2f2f2 55%,#e9e4dc 100%)"></div></div>
  <div class="abs thumb" style="left:606px"><div role="img" aria-label="Portfolio sample: cleaning company website with city skyline" style="background:linear-gradient(180deg,#1d3f9a 0%,#4f8fd6 45%,#e7eef6 75%,#ffffff 100%)"></div></div>
  <div class="abs thumb" style="left:808px"><div role="img" aria-label="Portfolio sample: garden nursery website with flowers and sky" style="background:linear-gradient(160deg,#ffffff 0%,#7fc0ee 45%,#d96a9e 75%,#eef3f0 100%)"></div></div>
  <svg class="abs arrow" style="left:1009px" width="14" height="56" viewBox="0 0 14 56" aria-hidden="true"><path d="M1 1l12 27L1 55" fill="none" stroke="#aaa" stroke-width="1.2"/></svg>

  <footer class="abs footer">
    <p class="copy">Copyright © 2014 Kestrel Tide Bureau. All Right Reserved &nbsp;|&nbsp; <b>Request Consultation</b></p>
    <div class="badge" aria-hidden="true"><i></i></div>
  </footer>

</div>
</body>
</html>
```